Verpackungsdesign für Parfüm gesucht
Zielgruppe
Wir werden eine Marke unter dem Namen ORMAL mit Parfüm auf dem Markt bringen und benötigen hierfür ein hochwertiges Design . Unsre Zielgruppe ist m/w/d und zwischen 16 und 60 Jahre.
Aufgabenstellung
Bei der Verpackung handelt es sich um eine Schiebeschachtel. Wir benötigen das Design nur für die Außenhülle, nicht für den Schuber.
Pflichtangaben auf der Verpackung sind unser Logo, Eau de Parfum, High Intense, 20 ml e 0.67 FL OZ,
Natural Spray Vaporisateur,

```html
<!DOCTYPE html>
<html lang="de">
<head>
<meta charset="UTF-8">
<title>ORMAL – High Intense Eau de Parfum</title>
<link href="https://fonts.googleapis.com/css2?family=EB+Garamond:wght@400;600&display=swap" rel="stylesheet">
<style>
  :root {
    --backdrop: #d6d5d5;
    --sleeve-dark: #1e1b1a;
    --sleeve-light: #4e4b48;
    --line-silver: #e4e4e4;
    --band-silver: #e9e9e9;
    --band-ink: #1f1c1b;
    --text-silver: #d8d8d8;
  }
  html, body {
    margin: 0;
    padding: 0;
    width: 1200px;
    height: 960px;
    overflow: hidden;
    background: var(--backdrop);
  }
  .canvas {
    position: relative;
    width: 1200px;
    height: 960px;
  }
  .sleeve-front {
    position: absolute;
    left: 370px;
    top: 90px;
    width: 460px;
    height: 780px;
    background: linear-gradient(90deg, var(--sleeve-dark) 0%, #2f2b29 55%, var(--sleeve-light) 100%);
    font-family: "EB Garamond", Georgia, serif;
  }
  .frame {
    position: absolute;
    inset: 20px;
    border: 3px solid var(--line-silver);
  }
  .brand-name {
    position: absolute;
    top: 210px;
    left: 0;
    right: 0;
    text-align: center;
    font-weight: 400;
    font-size: 84px;
    letter-spacing: 10px;
    color: var(--line-silver);
    line-height: 1;
  }
  .variant-band {
    position: absolute;
    left: 0;
    right: 0;
    top: 480px;
    height: 70px;
    background: var(--band-silver);
    display: flex;
    align-items: center;
    justify-content: center;
  }
  .variant-name {
    font-weight: 600;
    font-size: 30px;
    color: var(--band-ink);
  }
  .product-details {
    position: absolute;
    left: 0;
    right: 0;
    top: 580px;
    text-align: center;
    color: var(--text-silver);
    font-size: 24px;
    line-height: 1.35;
  }
  .product-details .product-type {
    font-weight: 600;
  }
  .product-details p {
    margin: 0;
  }
</style>
</head>
<body>
  <main class="canvas">
    <section class="sleeve-front">
      <div class="frame"></div>
      <h1 class="brand-name">ORMAL</h1>
      <div class="variant-band">
        <span class="variant-name">High Intense</span>
      </div>
      <div class="product-details">
        <p class="spray-note">Natural Spray Vaporisateur</p>
        <p class="product-type">Eau de Parfum</p>
        <p class="volume">0.67 FL OZ&nbsp;&nbsp;20 ML</p>
      </div>
    </section>
  </main>
</body>
</html>
```